Clearpath Ledger Billing Company Business card

Need a business card that stands out that includes name of company,(above) Owners name Marisol Whitfield phone#555-314-7762 email# ClearpathLedgerBC@mailbox-example.com and website www.Clearpathledgerbillingcompany-example.com. This is a medical billing company so the card has to relate to that or relate to steady cashflow

```html
<!DOCTYPE html>
<html lang="en">
<head>
<meta charset="utf-8">
<title>Clearpath Ledger Billing Company — Business Card</title>
<link rel="stylesheet" href="https://fonts.googleapis.com/css2?family=Questrial&display=swap">
<style>
  :root {
    --blue: #1f4fa3;
    --blue-deep: #173f8a;
    --blue-light: #2a5fbd;
    --green: #8fd14f;
    --white: #ffffff;
    --paper: #f4f5f7;
    --ink: #3a3f47;
    --stage: #e9eaec;
  }
  * { box-sizing: border-box; margin: 0; padding: 0; }
  html, body {
    width: 730px; height: 1200px; overflow: hidden;
    background: var(--stage);
    font-family: "Questrial", "Century Gothic", sans-serif;
  }
  .card {
    position: absolute;
    left: 45px;
    width: 640px; height: 366px;
    overflow: hidden;
    box-shadow: 0 8px 24px rgba(0,0,0,0.18);
  }
  .card--contact { top: 150px; background: linear-gradient(135deg, var(--blue-light), var(--blue-deep)); }
  .card--brand { top: 660px; background: linear-gradient(180deg, var(--white), var(--paper)); }

  /* contact side */
  .contact__accent {
    position: absolute; inset: 0;
    background: var(--green);
    clip-path: polygon(0 30%, 0 36%, 14% 0, 11% 0);
  }
  .contact__panel {
    position: absolute; inset: 0;
    background: linear-gradient(180deg, var(--white), var(--paper));
    clip-path: polygon(0 38%, 38% 38%, 44% 30%, 44% 100%, 0 100%);
  }
  .contact__brand {
    position: absolute; left: 30px; top: 200px; width: 230px;
    display: flex; align-items: center; gap: 10px;
  }
  .brand-mark { width: 14px; height: 14px; background: var(--green); flex: none; }
  .brand-name {
    color: var(--blue); font-size: 17px; line-height: 1.25; letter-spacing: 0.5px;
    text-transform: uppercase;
  }
  .nameplate {
    position: absolute; left: 300px; top: 40px; width: 300px; height: 88px;
    background: var(--green);
    padding: 16px 24px;
  }
  .nameplate__name { color: var(--white); font-size: 32px; line-height: 1.1; white-space: nowrap; }
  .nameplate__role { color: var(--blue); font-size: 14px; margin-top: 6px; }
  .details { position: absolute; left: 300px; top: 170px; right: 14px; list-style: none; }
  .details__item {
    display: flex; align-items: center; gap: 10px;
    color: var(--white); font-size: 14px; margin-bottom: 18px;
    white-space: nowrap;
  }
  .details__icon {
    width: 30px; height: 30px; border-radius: 6px; background: var(--green);
    display: flex; align-items: center; justify-content: center; flex: none;
  }
  .details__text { white-space: nowrap; }

  /* brand side */
  .brand__band {
    position: absolute; inset: 0;
    background: linear-gradient(135deg, var(--blue-light), var(--blue-deep));
    clip-path: polygon(80% 0, 100% 0, 100% 100%, 64% 100%);
  }
  .brand__stripe {
    position: absolute; inset: 0;
    background: var(--green);
    clip-path: polygon(78.5% 0, 80% 0, 64% 100%, 62.5% 100%);
  }
  .brand__identity {
    position: absolute; left: 60px; top: 110px; width: 360px;
    display: flex; align-items: center; gap: 14px;
  }
  .brand__identity .brand-mark { width: 18px; height: 18px; }
  .brand__identity .brand-name { font-size: 22px; }
  .brand__web {
    position: absolute; left: 60px; top: 250px;
    color: var(--ink); font-size: 14px; letter-spacing: 0.3px;
    white-space: nowrap;
  }
</style>
</head>
<body>
  <section class="card card--contact" aria-label="Business card, contact side">
    <div class="contact__accent"></div>
    <div class="contact__panel"></div>
    <div class="contact__brand">
      <span class="brand-mark"></span>
      <span class="brand-name">Clearpath Ledger Billing Company</span>
    </div>
    <div class="nameplate">
      <p class="nameplate__name">Marisol Whitfield</p>
      <p class="nameplate__role">Owners</p>
    </div>
    <ul class="details">
      <li class="details__item">
        <span class="details__icon">
          <svg width="18" height="18" viewBox="0 0 24 24" aria-hidden="true"><path fill="#fff" d="M6.6 10.8a15 15 0 0 0 6.6 6.6l2.2-2.2a1 1 0 0 1 1-.25 11.4 11.4 0 0 0 3.6.57 1 1 0 0 1 1 1V20a1 1 0 0 1-1 1A17 17 0 0 1 3 4a1 1 0 0 1 1-1h3.5a1 1 0 0 1 1 1c0 1.25.2 2.46.57 3.6a1 1 0 0 1-.25 1z"/></svg>
        </span>
        <span class="details__text">555-314-7762</span>
      </li>
      <li class="details__item">
        <span class="details__icon">
          <svg width="18" height="18" viewBox="0 0 24 24" aria-hidden="true"><rect x="3" y="6" width="18" height="12" rx="1" fill="none" stroke="#fff" stroke-width="2"/><path d="M3 7l9 6 9-6" fill="none" stroke="#fff" stroke-width="2"/></svg>
        </span>
        <span class="details__text">ClearpathLedgerBC@mailbox-example.com</span>
      </li>
    </ul>
  </section>

  <section class="card card--brand" aria-label="Business card, brand side">
    <div class="brand__band"></div>
    <div class="brand__stripe"></div>
    <div class="brand__identity">
      <span class="brand-mark"></span>
      <span class="brand-name">Clearpath Ledger Billing Company</span>
    </div>
    <p class="brand__web">www.Clearpathledgerbillingcompany-example.com</p>
  </section>
</body>
</html>
```